Amazing Real Estate Branding and Client Capture

Please improve, redesign, and complete BrannokVell.com with creative input into various pages including the buy, sell, and giving back pages. I already have a Home Page I am happy with. ****Please focus on the buy, sell, and giving back pages. *** This website is used to impress potential clients with a focus on high priced home sellers. The style should be similar to my client welcome kit and other marketing materials I use which I will attach under uploads. However, it should not be a direct copy of my client welcome kit. The sell page needs to have reasons to hire me and should have past sales (photos are in powerpoint upload) like my client welcome kit. There is also a video in my powerpoint to put in sell section as well. Powerpoint can be viewed at https://www.filquarry.net/scl/fi/zq4ra1tuv7kx902mpw218/PitchBoard.pptx?dl=0&rlkey=tu8wbx3npq5qz631mnr0bxtej Pages should be clean, modern, and user friendly for an elderly community. I am ok with sub pages as needed. Color palette should follow the Ho/Vel Secondary colors. Thank you so much!

Target Market(s)

Luxury Real Estate Clients

Industry/Entity Type

Real Estate

Font styles to use
Serif
Sans Serif

Requirements
Must have
• Modern easy to use theme
Nice to have
• Strategy to impress possible client and capture contact info
Should not have
• Basic, simple, or cheap appearance

```html
<!DOCTYPE html>
<html lang="en">
<head>
<meta charset="utf-8">
<title>Sell | Brannok Vell</title>
<link rel="stylesheet" href="https://fonts.googleapis.com/css2?family=Cinzel:wght@400;700;800&family=Open+Sans:wght@400;600;700&display=swap">
<style>
:root{
  --navy:#14366f;
  --navy-deep:#0b2b66;
  --red:#d4192e;
  --ink:#222;
  --text:#555;
  --label:#333;
  --line:#c9c9c9;
  --mist:#f1f1f1;
  --white:#fff;
}
*{box-sizing:border-box;margin:0;padding:0}
html,body{width:1200px;height:4360px;overflow:hidden}
body{position:relative;background:var(--white);font-family:"Open Sans",Arial,sans-serif;color:var(--text)}
.abs{position:absolute}
.caps{text-transform:uppercase}

/* header */
.hero-photo{left:0;top:0;width:1200px;height:440px;background:linear-gradient(180deg,#2d5a8c 0%,#6f87a3 35%,#b37a55 60%,#5a4a38 85%,#2e3a2a 100%)}
.header-band{left:0;top:0;width:1200px;height:149px;background:rgba(20,54,111,.92)}
.contact-bar{right:0;top:0;width:640px;height:47px;background:var(--red);clip-path:polygon(4% 0,100% 0,100% 100%,6% 100%);display:flex;align-items:center;justify-content:flex-end;padding-right:112px;gap:14px;color:var(--white);font-size:17px;font-weight:600;white-space:nowrap}
.contact-bar svg{width:16px;height:16px;vertical-align:-2px;margin-right:6px}
.brand{left:110px;top:58px;display:flex;align-items:center;gap:12px}
.brand-ring{width:24px;height:24px;border:3px solid var(--white);border-radius:50%;flex:none}
.brand-name{font-family:"Cinzel",Georgia,serif;font-weight:700;font-size:28px;color:var(--white);line-height:1.1;white-space:nowrap}
.main-nav{left:420px;top:86px;display:flex;gap:16px;font-size:15px;font-weight:600;color:var(--white);white-space:nowrap}
.main-nav .current{color:var(--red)}
.page-title{left:107px;top:232px;font-family:"Cinzel",Georgia,serif;font-weight:700;font-size:86px;line-height:100px;color:var(--white);letter-spacing:1px}
.swoosh{left:0;top:360px;width:1200px;height:90px}

/* services */
.services-bg{left:0;top:440px;width:1200px;height:740px;background:linear-gradient(180deg,#e9e9e9 0%,#f3f3f3 60%,#ececec 100%)}
.headline{left:0;top:500px;width:1200px;text-align:center;font-family:"Cinzel",Georgia,serif;font-weight:700;color:var(--ink);text-transform:uppercase}
.headline .small{font-size:48px;line-height:62px}
.headline .big{font-size:66px;line-height:80px}
.red{color:var(--red)}
.partner-mark{left:912px;top:486px;font-family:"Open Sans",Arial,sans-serif;font-weight:700;font-size:22px;color:var(--navy);white-space:nowrap}
.checklist{list-style:none;font-size:16px;line-height:20px;color:var(--text);white-space:nowrap}
.checklist li{position:relative;padding-left:32px;margin-bottom:19px}
.checklist li::before{content:"";position:absolute;left:0;top:1px;width:17px;height:17px;border-radius:50%;background:var(--red)}
.checklist li::after{content:"";position:absolute;left:5px;top:5px;width:6px;height:3px;border-left:2px solid var(--white);border-bottom:2px solid var(--white);transform:rotate(-45deg)}

/* video */
.video{left:317px;top:1114px;width:567px;height:313px;background:#000;display:flex;align-items:center;justify-content:center;gap:80px;box-shadow:0 4px 14px rgba(0,0,0,.25)}
.video-name{font-size:36px;font-weight:700;color:var(--white);line-height:1}
.play{position:absolute;left:250px;top:123px;width:68px;height:68px;border-radius:50%;background:rgba(40,40,40,.9);border:2px solid #ddd}
.play::after{content:"";position:absolute;left:26px;top:20px;border-left:20px solid var(--white);border-top:13px solid transparent;border-bottom:13px solid transparent}

/* results */
.section-title{left:0;top:1496px;width:1200px;text-align:center;font-family:"Cinzel",Georgia,serif;font-weight:700;font-size:50px;line-height:64px;color:var(--ink);text-transform:uppercase}
.slider{left:112px;top:1603px;width:976px;height:454px;background:var(--white);box-shadow:0 3px 14px rgba(0,0,0,.3)}
.slide-photo{left:10px;top:10px;width:956px;height:434px;background:linear-gradient(180deg,#4a4f6a 0%,#b27468 30%,#5d6c6a 55%,#2e3f33 80%,#1f2a22 100%)}
.arrow{top:187px;width:60px;height:60px;border-radius:50%;background:rgba(0,0,0,.55)}
.arrow svg{width:60px;height:60px}
.sale-tag{left:657px;top:327px;width:309px;height:117px;background:rgba(212,25,46,.85);padding:12px 0 0 35px;color:var(--white)}
.sale-tag strong{display:block;font-size:33px;font-weight:700;line-height:40px}
.sale-tag span{display:block;font-size:18px;line-height:28px}

/* form */
.form-bg{left:0;top:2137px;width:1200px;height:1830px;background:var(--mist)}
.form-frame{left:110px;top:2240px;width:978px;height:1642px;border:2px solid #b5b5b5}
.form-head{left:257px;top:2212px;width:686px;height:130px;background:var(--mist);text-align:center;font-family:"Cinzel",Georgia,serif;font-weight:700;color:var(--ink);text-transform:uppercase}
.form-head .l1{font-size:48px;line-height:62px;padding-top:18px}
.form-head .l2{font-size:48px;line-height:58px;color:var(--red)}
.form-intro{left:200px;top:2356px;width:800px;text-align:center;font-size:16px;line-height:29px;color:var(--text)}
.label{left:165px;font-size:16px;font-weight:600;color:var(--label);white-space:nowrap}
.field{background:var(--white);border:1px solid var(--line)}
.radio{font-size:16px;color:#888;display:flex;align-items:flex-start;gap:6px;line-height:29px}
.radio i{display:inline-block;width:14px;height:14px;border:2px solid #888;border-radius:50%;margin-top:7px;position:relative;flex:none}
.radio.on i::after{content:"";position:absolute;left:2px;top:2px;width:6px;height:6px;border-radius:50%;background:#777}
.submit{left:532px;top:3782px;width:137px;height:63px;border-radius:32px;background:var(--red);color:var(--white);font-size:19px;font-weight:700;display:flex;align-items:center;justify-content:center}

/* footer */
.footer-shape{left:0;top:3925px;width:1200px;height:435px}
.footer-brand{left:0;top:4105px;width:1200px;display:flex;justify-content:center;align-items:center;gap:12px}
.footer-brand .brand-name{font-size:34px}
.footer-nav{left:0;top:4236px;width:1200px;display:flex;justify-content:center;gap:13px;font-size:16px;color:var(--white);white-space:nowrap}
.footer-nav em{font-style:normal;opacity:.8}
.social{left:0;top:4300px;width:1200px;display:flex;justify-content:center;align-items:center;gap:10px;color:var(--white);font-size:16px;font-weight:600}
.social i{width:22px;height:22px;border:2px solid var(--white);border-radius:50%}
</style>
</head>
<body>

<header>
  <div class="abs hero-photo" role="img" aria-label="Photo of a tile-roofed Florida home with palm trees at twilight"></div>
  <div class="abs header-band"></div>
  <div class="abs contact-bar">
    <span><svg viewBox="0 0 24 24" fill="#fff"><path d="M6.6 10.8a15 15 0 0 0 6.6 6.6l2.2-2.2a1 1 0 0 1 1-.25 11.4 11.4 0 0 0 3.6.57 1 1 0 0 1 1 1V20a1 1 0 0 1-1 1A17 17 0 0 1 3 4a1 1 0 0 1 1-1h3.5a1 1 0 0 1 1 1c0 1.25.2 2.45.57 3.57a1 1 0 0 1-.25 1z"/></svg>(941) 555 - 0182</span>
    <span>|</span>
    <span><svg viewBox="0 0 24 24" fill="none" stroke="#fff" stroke-width="2"><path d="M3 6h18v12H3z M3 6l9 7 9-7"/></svg>BrannokVell@HoVel.net</span>
  </div>
  <div class="abs brand"><div class="brand-ring"></div><div class="brand-name">Brannok Vell</div></div>
  <nav class="abs main-nav"><span>About</span><span>Buy</span><span class="current">Sell</span><span>Photography</span><span>Giving Back</span><span>Testimonials</span><span>Welcome Kit</span><span>Contact Us</span></nav>
  <h1 class="abs page-title">SELL</h1>
  <svg class="abs swoosh" viewBox="0 0 1200 90" preserveAspectRatio="none">
    <path d="M0 80 Q600 -10 1200 60 L1200 90 L0 90Z" fill="#14366f"/>
    <path d="M0 84 Q600 10 1200 72 L1200 90 L0 90Z" fill="#ffffff"/>
    <path d="M0 90 Q600 30 1200 86 L1200 90Z" fill="#e9e9e9"/>
  </svg>
</header>

<section class="services">
  <div class="abs services-bg" role="img" aria-label="Faded photo of a screened pool lanai"></div>
  <h2 class="abs headline"><div class="small">Doing More From</div><div class="big">For Sale To <span class="red">Sold</span></div></h2>
  <div class="abs partner-mark">HoVel Realty</div>

  <ul class="abs checklist" style="left:110px;top:690px">
    <li>High Definition Professional<br>Photos</li>
    <li>Enhanced MLS Listing</li>
    <li>Large Sign Post in Yard</li>
    <li>Electronic Lockbox</li>
    <li>Available 24/7</li>
    <li>Multiple Agents Work For You</li>
    <li>Scheduled Updates</li>
    <li>Photography Preparation<br>Checklist</li>
    <li>In Depth Marketing Plan</li>
  </ul>
  <ul class="abs checklist" style="left:435px;top:690px">
    <li>Full Time Transaction Coordinator<br>Soft Staging</li>
    <li>Social Media Campaign Generating<br>1000s of Views</li>
    <li>Listing Posted in All Local<br>Friendhub Groups</li>
    <li>Custom Single Property Website</li>
    <li>Fully Interactive 3D Spacewend<br>Tour</li>
    <li>Aerial Images With 4K Drone</li>
    <li>Twilight Photography</li>
  </ul>
  <ul class="abs checklist" style="left:799px;top:690px">
    <li>Sunset Photography</li>
    <li>Door to Door Campaign in<br>Neighborhood</li>
    <li>Direct Mail Campaign in<br>Neighborhood</li>
    <li>Email Blast to 1000+ Agents</li>
    <li>Schematic Floor-plan With<br>Room Measurements</li>
    <li>Online Dollhouse View</li>
    <li>Professional Booklets For Buyers<br>During Showings</li>
    <li>Feedback Reports From Showings</li>
  </ul>

  <div class="abs video" role="img" aria-label="Video player for a 3D home tour">
    <span class="video-name">Space</span><span class="video-name">wend</span>
    <div class="play"></div>
  </div>
</section>

<section class="results">
  <h2 class="abs section-title">Proven <span class="red">Results</span></h2>
  <div class="abs slider">
    <div class="abs slide-photo" role="img" aria-label="Aerial sunset photo of waterfront homes among mangrove islands"></div>
    <div class="abs arrow" style="left:-18px"><svg viewBox="0 0 60 60"><path d="M35 20 L25 30 L35 40" stroke="#fff" stroke-width="4" fill="none"/></svg></div>
    <div class="abs arrow" style="right:-18px"><svg viewBox="0 0 60 60"><path d="M25 20 L35 30 L25 40" stroke="#fff" stroke-width="4" fill="none"/></svg></div>
    <div class="abs sale-tag"><strong>$1,100,000</strong><span>Sold in only 22 Days</span><span>Over Asking Price</span></div>
  </div>
</section>

<section class="seller-form">
  <div class="abs form-bg"></div>
  <div class="abs form-frame"></div>
  <h2 class="abs form-head"><div class="l1">Considering</div><div class="l2">Selling Your Home?</div></h2>
  <p class="abs form-intro">Our biggest priority is being able to provide you with a 5 star experience!<br>In order to better serve you please take 5 minutes to fill out the form below so we may better understand how to help you with your home sale.</p>

  <div class="abs label" style="top:2474px">First Name</div>
  <div class="abs label" style="left:606px;top:2474px">Last Name</div>
  <div class="abs field" style="left:166px;top:2511px;width:427px;height:50px"></div>
  <div class="abs field" style="left:606px;top:2511px;width:427px;height:50px"></div>

  <div class="abs label" style="top:2578px">Email</div>
  <div class="abs label" style="left:606px;top:2578px">Phone</div>
  <div class="abs field" style="left:166px;top:2614px;width:427px;height:50px"></div>
  <div class="abs field" style="left:606px;top:2614px;width:427px;height:50px"></div>

  <div class="abs label" style="top:2684px">Preferred method of communication</div>
  <div class="abs radio on" style="left:165px;top:2724px"><i></i>Text</div>
  <div class="abs radio" style="left:367px;top:2724px"><i></i>Call</div>
  <div class="abs radio" style="left:576px;top:2724px"><i></i>Email</div>
  <div class="abs radio" style="left:801px;top:2724px"><i></i>Friendhub Messenger</div>

  <div class="abs label" style="top:2777px">Property Address</div>
  <div class="abs field" style="left:166px;top:2814px;width:867px;height:51px"></div>

  <div class="abs label" style="top:2889px">What is your ideal time frame for moving?</div>
  <div class="abs radio on" style="left:165px;top:2929px"><i></i>ASAP</div>
  <div class="abs radio" style="left:367px;top:2929px"><i></i>1-3 Months</div>
  <div class="abs radio" style="left:576px;top:2929px"><i></i>4-7 Months</div>
  <div class="abs radio" style="left:801px;top:2929px"><i></i>8-12 Months</div>

  <div class="abs label" style="top:2981px">Please briefly describe the home including any update and improvements</div>
  <div class="abs field" style="left:166px;top:3017px;width:867px;height:93px"></div>

  <div class="abs label" style="top:3135px">What is your favourite aspect of your home?</div>
  <div class="abs field" style="left:166px;top:3171px;width:867px;height:93px"></div>

  <div class="abs label" style="top:3289px">In your opinion, how would you describe the overall condition of the property?</div>
  <div class="abs radio on" style="left:165px;top:3330px"><i></i>Below Average</div>
  <div class="abs radio" style="left:367px;top:3330px"><i></i>Average</div>
  <div class="abs radio" style="left:679px;top:3330px"><i></i>Above Average</div>

  <div class="abs label" style="top:3384px">What is your current estimation of the home’s value in today’s market?</div>
  <div class="abs field" style="left:166px;top:3420px;width:867px;height:51px"></div>

  <div class="abs label" style="top:3495px">Are you planning on purchasing another property?</div>
  <div class="abs radio on" style="left:165px;top:3535px"><i></i>No</div>
  <div class="abs radio" style="left:367px;top:3535px;width:250px"><i></i><span>Yes, and need to sell it in order to purchase next home</span></div>
  <div class="abs radio" style="left:679px;top:3535px;width:300px"><i></i><span>Yes, but don’t have to sell this one in order to buy the next</span></div>

  <div class="abs label" style="top:3621px">Do you have any other questions or concerns?</div>
  <div class="abs field" style="left:166px;top:3657px;width:867px;height:93px"></div>

  <div class="abs submit">SUBMIT</div>
</section>

<footer>
  <svg class="abs footer-shape" viewBox="0 0 1200 435" preserveAspectRatio="none">
    <path d="M0 100 Q420 70 600 0 Q780 70 1200 100 L1200 435 L0 435Z" fill="#0b2b66"/>
  </svg>
  <div class="abs footer-brand"><div class="brand-ring"></div><div class="brand-name">Brannok Vell</div></div>
  <nav class="abs footer-nav"><span>Home</span><em>|</em><span>About</span><em>|</em><span>Buy</span><em>|</em><span>Sell</span><em>|</em><span>Photography</span><em>|</em><span>Giving Back</span><em>|</em><span>Testimonials</span><em>|</em><span>Welcome Kit</span><em>|</em><span>Contact Us</span></nav>
  <div class="abs social"><i></i><span>Friendhub</span></div>
</footer>

</body>
</html>
```